Tulven Electrics Flyer Design Advertising

I am after an A5 Flyer design to help promote my electrical services business.
I would like to have information on what my business offers, photos of electrical work, and specials/deals for an amount of time.

Industry/Entity Type

Electrician

Font styles to use
Sans Serif

Colors
0292cd
33a6d7
85cae6
3176b5
333333
1b1b1b
ffffff
5c5c5c
474747

Requirements
Must have
• Specialising in New homes, renovations and commercial projects
• Contact details:
• ph. 0437 619 458
• email admin@tulvenelectrics.example.au
• facebook TulvenElectrics
• Specials/Deals:
• 10% off all electrical services
• or
• Free LED downlights on installation
• *Terms conditions apply
• ALL RESIDENTIAL & COMMERCIAL ELECTRICAL SERVICES
• - New Home installations
• - Commercial projects
• - Shop fit outs
• - Renovations
• - Smoke Detectors
• - Air Conditioning and Ceiling Fans
• - Garden Lighting
• - Oven and Cooktop Installations
• - Power Point installation
• - LED lighting upgrades
• - Security Lighting
• - Switchboard upgrades
• - Test and Tag
• - Commercial Property
• - General Electrical Maintenance

```html
<!DOCTYPE html>
<html lang="en">
<head>
<meta charset="utf-8">
<title>Tulven Electrics – Flyer</title>
<link rel="stylesheet" href="https://fonts.googleapis.com/css2?family=Oswald:wght@500;600&family=Lato:wght@400;700&display=swap">
<style>
  :root {
    --blue: #1fa9e1;
    --blue-deep: #0292cd;
    --blue-soft: #85cae6;
    --ink: #333333;
    --ink-dark: #1b1b1b;
    --ink-mid: #474747;
    --grey-light: #e6e6e8;
    --white: #ffffff;
    --red: #e41e2b;
  }
  * { box-sizing: border-box; margin: 0; padding: 0; }
  html, body { width: 987px; height: 1200px; overflow: hidden; background: var(--grey-light); }
  .flyer { position: relative; width: 987px; height: 1200px; overflow: hidden; font-family: "Lato", sans-serif; }
  .flyer__shapes { position: absolute; inset: 0; }

  .brand { position: absolute; left: 560px; top: 22px; display: flex; align-items: center; gap: 16px; }
  .brand__dot { width: 140px; height: 140px; border-radius: 50%; background: var(--blue); }
  .brand__name { font-family: "Oswald", sans-serif; font-weight: 600; font-size: 40px; line-height: 1.05; color: var(--ink); text-transform: uppercase; }

  .offer-ribbon { position: absolute; left: 760px; top: 206px; width: 158px; height: 186px; background: var(--blue);
    clip-path: polygon(0 0, 100% 0, 100% 100%, 50% 86%, 0 100%);
    font-family: "Oswald", sans-serif; font-weight: 500; color: var(--white); text-align: center; text-transform: uppercase; padding-top: 10px; }
  .offer-ribbon__lead { font-size: 32px; line-height: 1.1; }
  .offer-ribbon__line { font-size: 24px; line-height: 1.35; }

  .services-heading { position: absolute; left: 0; top: 662px; width: 431px; height: 55px; background: var(--grey-light);
    padding: 6px 0 0 73px; font-size: 18px; font-weight: 400; line-height: 1.35; color: var(--ink-dark); text-transform: uppercase; }
  .services-list { position: absolute; left: 75px; top: 734px; list-style: none; }
  .services-list li { font-size: 17px; line-height: 21.9px; color: var(--white); padding-left: 21px; position: relative; }
  .services-list li::before { content: ""; position: absolute; left: 2px; top: 6px; width: 9px; height: 9px;
    border-right: 2px solid var(--white); border-top: 2px solid var(--white); transform: rotate(45deg); }

  .discount-badge { position: absolute; left: 470px; top: 918px; width: 172px; height: 168px; background: var(--red);
    clip-path: polygon(100% 50%,93.2% 58.6%,96.2% 69.2%,86.6% 74.5%,85.4% 85.4%,74.5% 86.6%,69.2% 96.2%,58.6% 93.2%,50% 100%,41.4% 93.2%,30.8% 96.2%,25.5% 86.6%,14.6% 85.4%,13.4% 74.5%,3.8% 69.2%,6.8% 58.6%,0 50%,6.8% 41.4%,3.8% 30.8%,13.4% 25.5%,14.6% 14.6%,25.5% 13.4%,30.8% 3.8%,41.4% 6.8%,50% 0,58.6% 6.8%,69.2% 3.8%,74.5% 13.4%,85.4% 14.6%,86.6% 25.5%,96.2% 30.8%,93.2% 41.4%);
    display: flex; align-items: center; justify-content: center; }
  .discount-badge__ring { width: 142px; height: 138px; border-radius: 50%; border: 2px solid var(--white);
    display: flex; flex-direction: column; align-items: center; justify-content: center; color: var(--white); text-align: center; }
  .discount-badge__value { font-family: "Oswald", sans-serif; font-weight: 500; font-size: 36px; line-height: 1; }
  .discount-badge__note { font-size: 17px; line-height: 1.4; margin-top: 4px; }

  .gallery__photo { position: absolute; left: 702px; width: 262px; }

  .contact { position: absolute; left: 20px; color: var(--white); display: flex; align-items: center; gap: 10px; }
  .contact--phone { top: 1110px; font-family: "Oswald", sans-serif; font-weight: 500; font-size: 30px; }
  .contact--email { top: 1150px; font-size: 15px; }
  .contact--social { left: 292px; top: 1150px; font-size: 17px; }
  .contact__square { width: 20px; height: 20px; background: var(--white); border-radius: 3px; }
</style>
</head>
<body>
<main class="flyer">
  <svg class="flyer__shapes" width="987" height="1200" viewBox="0 0 987 1200" aria-hidden="true">
    <defs>
      <linearGradient id="heroTone" x1="0" y1="0" x2="0.4" y2="1">
        <stop offset="0" stop-color="#6d7d9a"/>
        <stop offset="0.45" stop-color="#c9b8a4"/>
        <stop offset="0.75" stop-color="#8a5a36"/>
        <stop offset="1" stop-color="#3f5a2a"/>
      </linearGradient>
    </defs>
    <!-- blue body -->
    <polygon points="0,600 987,480 987,1200 0,1200" fill="var(--blue)"/>
    <!-- white divider under hero -->
    <polygon points="390,600 987,500 987,520 396,620" fill="var(--white)"/>
    <!-- bottom white band and dark footer -->
    <polygon points="0,1015 987,1170 987,1200 0,1200" fill="var(--white)"/>
    <polygon points="0,1043 880,1200 0,1200" fill="var(--ink)"/>
    <!-- top accent stripe -->
    <polygon points="148,17 987,296 987,316 160,30" fill="var(--blue)"/>
    <!-- services heading accent -->
    <polygon points="416,662 462,662 476,717 430,717" fill="var(--ink)"/>
    <polygon points="442,662 450,662 464,717 456,717" fill="var(--blue)"/>
    <!-- gallery backing frame -->
    <polygon points="694,536 972,530 972,1172 694,1142" fill="var(--white)" opacity="0.9"/>
    <rect x="686" y="640" width="4" height="460" fill="var(--white)"/>
  </svg>

  <svg class="flyer__shapes" width="987" height="1200" viewBox="0 0 987 1200" role="img" aria-label="Photo of a covered outdoor deck at dusk with glowing LED downlights, palm trees and a house behind">
    <polygon points="0,0 30,0 987,318 987,490 0,634" fill="url(#heroTone)"/>
  </svg>

  <div class="brand">
    <span class="brand__dot"></span>
    <span class="brand__name">Tulven<br>Electrics</span>
  </div>

  <div class="offer-ribbon">
    <div class="offer-ribbon__lead">Free LED</div>
    <div class="offer-ribbon__line">Downlights</div>
    <div class="offer-ribbon__line">On</div>
    <div class="offer-ribbon__line">Installation</div>
  </div>

  <h2 class="services-heading">All Residential &amp; Commercial<br>Electrical Services</h2>
  <ul class="services-list">
    <li>New Home installations</li>
    <li>Shop fit outs</li>
    <li>Renovations</li>
    <li>Smoke Detectors</li>
    <li>Air Conditioning and Ceiling Fans</li>
    <li>Garden Lighting</li>
    <li>Oven and Cooktop Installations</li>
    <li>Power Point installation</li>
    <li>LED lighting upgrades</li>
    <li>Security Lighting</li>
    <li>Switchboard upgrades</li>
    <li>Test and Tag</li>
    <li>General Electrical Maintenance</li>
  </ul>

  <div class="discount-badge">
    <div class="discount-badge__ring">
      <span class="discount-badge__value">10% OFF</span>
      <span class="discount-badge__note">any electrical<br>work</span>
    </div>
  </div>

  <div class="gallery">
    <div class="gallery__photo" style="top:542px;height:170px;background:linear-gradient(160deg,#f2f0ec,#b9b2a8 70%,#6b5a4a);" role="img" aria-label="Photo of a bright modern kitchen with pendant lights and bar stools"></div>
    <div class="gallery__photo" style="top:717px;height:130px;background:linear-gradient(180deg,#2f3a33,#d8cbb4 50%,#6a4a32);" role="img" aria-label="Photo of an evening courtyard lounge lit by wall lights"></div>
    <div class="gallery__photo" style="top:854px;height:131px;background:linear-gradient(170deg,#f4f4f2,#d9d4c8 60%,#9a8a70);" role="img" aria-label="Photo of a light-filled open living room with a ceiling fan"></div>
    <div class="gallery__photo" style="top:989px;height:165px;background:linear-gradient(180deg,#e6e8ea,#9aa2a8 50%,#4b5a3a);" role="img" aria-label="Photo of a renovated timber house with lit windows at dusk"></div>
  </div>

  <div class="contact contact--phone">
    <svg width="28" height="24" viewBox="0 0 28 24" aria-hidden="true"><path d="M2 8 Q14 -2 26 8 L22 11 L19 8 Q14 5 9 8 L6 11 Z M6 12 H22 L25 22 H3 Z" fill="var(--white)"/></svg>
    <span>0437 619 458</span>
  </div>
  <div class="contact contact--email">
    <svg width="22" height="16" viewBox="0 0 22 16" aria-hidden="true"><rect x="1" y="1" width="20" height="14" fill="none" stroke="var(--white)" stroke-width="1.5"/><path d="M1 1 L11 9 L21 1" fill="none" stroke="var(--white)" stroke-width="1.5"/></svg>
    <span>admin@tulvenelectrics.example.au</span>
  </div>
  <div class="contact contact--social">
    <span class="contact__square"></span>
    <span>TulvenElectrics</span>
  </div>
</main>
</body>
</html>
```